Modern Lawfirm Business Card Design

We're looking for a business card to incorporate the newly created logo we had made.

Ideally looking for a law firm business card demonstrating, modern, minimalist, strong/bold design.

I'm open to any design honestly, but nothing "flashy".

Target Market(s)

Immigration law, family immigration, humanitarian, general legal

Industry/Entity Type

Law Firm

Contact Information for Business Card

Please use dummy information, name, street address, city, state, phone number, email, website.

Font styles to use
Serif
Sans Serif

Requirements
Must have
• Please use dummy information, name, street address, city, state, phone number, email, website.

```html
<!DOCTYPE html>
<html lang="en">
<head>
<meta charset="utf-8">
<title>Halvorsen Immigration Law – Business Card</title>
<link href="https://fonts.googleapis.com/css2?family=Cinzel:wght@500&family=Fira+Sans:wght@400;500&display=swap" rel="stylesheet">
<style>
  :root {
    --blue: #145a96;
    --blue-deep: #0f4c82;
    --paper: #f3f3f1;
    --ink-light: #ffffff;
    --backdrop-top: #e6e9ef;
    --backdrop-bottom: #a9b0bd;
  }
  * { margin: 0; padding: 0; box-sizing: border-box; }
  html, body { width: 1200px; height: 1000px; overflow: hidden; }
  body {
    background: linear-gradient(160deg, var(--backdrop-top), var(--backdrop-bottom));
    font-family: "Fira Sans", sans-serif;
    display: flex;
    align-items: center;
    justify-content: center;
    gap: 40px;
  }
  .card {
    width: 540px;
    height: 309px;
    border-radius: 3px;
    overflow: hidden;
    box-shadow: 0 14px 30px rgba(30, 40, 60, 0.25);
  }
  .card-front { display: flex; }
  .front-brand {
    width: 42%;
    background: var(--paper);
    display: flex;
    align-items: center;
    justify-content: center;
  }
  .front-details {
    width: 58%;
    background: var(--blue);
    color: var(--ink-light);
    padding: 26px 22px 0 26px;
  }
  .wordmark {
    font-family: "Cinzel", serif;
    font-weight: 500;
    text-align: center;
    line-height: 1.25;
    letter-spacing: 1px;
    display: flex;
    align-items: center;
    gap: 8px;
  }
  .wordmark-square { width: 10px; height: 10px; flex: none; }
  .front-brand .wordmark { color: var(--blue); font-size: 17px; }
  .front-brand .wordmark-square { background: var(--blue); }
  .holder-name {
    font-family: "Cinzel", serif;
    font-weight: 500;
    font-size: 21px;
    letter-spacing: 1px;
    line-height: 1.1;
  }
  .holder-title { font-size: 12px; font-weight: 500; margin-top: 2px; }
  .address { font-size: 13px; line-height: 1.4; margin-top: 20px; }
  .contact-list { list-style: none; margin-top: 14px; }
  .contact-item {
    display: flex;
    align-items: center;
    gap: 8px;
    font-size: 13px;
    height: 23px;
  }
  .contact-icon { width: 15px; height: 15px; flex: none; }
  .card-back {
    background: var(--blue-deep);
    display: flex;
    align-items: center;
    justify-content: center;
  }
  .card-back .wordmark {
    color: var(--paper);
    font-size: 19px;
  }
  .card-back .wordmark-square { background: var(--paper); }
</style>
</head>
<body>

<section class="card card-front" aria-label="Business card front">
  <div class="front-brand">
    <div class="wordmark"><span class="wordmark-square"></span><span>Halvorsen<br>Immigration Law</span></div>
  </div>
  <div class="front-details">
    <h1 class="holder-name">MARA LINDQVIST</h1>
    <p class="holder-title">Attorney &amp; Counselor at law</p>
    <p class="address">1847 Alder Creek Rd, Maple Run,<br>PA, 18090</p>
    <ul class="contact-list">
      <li class="contact-item">
        <svg class="contact-icon" viewBox="0 0 16 16"><circle cx="8" cy="8" r="8" fill="#fff"/><path d="M5.2 4.3l1.4-.3.8 2-1 .8a5 5 0 0 0 2.6 2.6l.8-1 2 .8-.3 1.4c-3.4.4-6.7-2.9-6.3-6.3z" fill="#145a96"/></svg>
        555-301-2846
      </li>
      <li class="contact-item">
        <svg class="contact-icon" viewBox="0 0 16 16"><circle cx="8" cy="8" r="8" fill="#fff"/><rect x="5.5" y="3.5" width="5" height="9" rx="1" fill="none" stroke="#145a96" stroke-width="1.2"/><circle cx="8" cy="11" r=".6" fill="#145a96"/></svg>
        555-418-7731
      </li>
      <li class="contact-item">
        <svg class="contact-icon" viewBox="0 0 16 16"><circle cx="8" cy="8" r="8" fill="#fff"/><rect x="4" y="6" width="8" height="5" rx="1" fill="#145a96"/><rect x="5.5" y="3.8" width="5" height="2.2" fill="#145a96"/><rect x="5.5" y="9" width="5" height="3" fill="#fff" stroke="#145a96" stroke-width=".8"/></svg>
        555-276-0953
      </li>
      <li class="contact-item">
        <svg class="contact-icon" viewBox="0 0 16 16"><circle cx="8" cy="8" r="8" fill="#fff"/><rect x="4" y="5" width="8" height="6" fill="none" stroke="#145a96" stroke-width="1.1"/><path d="M4 5l4 3.2L12 5" fill="none" stroke="#145a96" stroke-width="1.1"/></svg>
        www.lindqvistlegal.com
      </li>
      <li class="contact-item">
        <svg class="contact-icon" viewBox="0 0 16 16"><circle cx="8" cy="8" r="8" fill="#fff"/><path d="M4 8l4-3.5L12 8h-1.2v3.5H5.2V8z" fill="#145a96"/></svg>
        mara@lindqvistlegal.com
      </li>
    </ul>
  </div>
</section>

<section class="card card-back" aria-label="Business card back">
  <div class="wordmark"><span class="wordmark-square"></span><span>Halvorsen<br>Immigration Law</span></div>
</section>

</body>
</html>
```